New Business Cards for Velmora

About Velmora:
At Velmora, we're more than just a company—we're a force for positive change in the staffing industry. Our brand is our heartbeat, and we need a designer who can translate that into every design element.

The Project:
We're revamping our business cards and need your artistic flair to make them stand out. Here's what we're looking for:

- Incorporate our existing brand elements (logo, colours, fonts) into the design.
- Craft a design that's sleek, professional, and memorable.
- Provide options for different layouts and finishes.
- Collaborate closely with our team to ensure the final product exceeds expectations.

Please note: For general text, we use Avenir. The brand guidelines are slightly out of date and don't have correct imaging. Colours are correct though.

```html
<!DOCTYPE html>
<html lang="en">
<head>
<meta charset="utf-8">
<title>Velmora Business Cards</title>
<link rel="stylesheet" href="https://fonts.googleapis.com/css2?family=Nunito+Sans:wght@400;600&family=Montserrat:wght@700&display=swap">
<style>
  :root {
    --canvas-bg: #232323;
    --card-bg: #1f1e23;
    --card-back-bg: #1c1b1f;
    --emboss: #111013;
    --brand-purple: #7a4aa0;
    --brand-pink: #e2197e;
    --text-light: #f2f0f4;
    --text-muted: #d9d6dd;
  }
  * { box-sizing: border-box; margin: 0; padding: 0; }
  html, body { width: 1200px; height: 780px; overflow: hidden; }
  body {
    background: var(--canvas-bg);
    font-family: "Nunito Sans", Arial, sans-serif;
    display: flex;
    align-items: center;
    justify-content: center;
    gap: 40px;
  }
  .card {
    position: relative;
    width: 520px;
    height: 300px;
    border-radius: 2px;
    overflow: hidden;
    box-shadow: 0 18px 40px rgba(0,0,0,.45);
  }
  .card--front { background: var(--card-bg); }
  .card--back {
    background: var(--card-back-bg);
    display: flex;
    align-items: center;
    justify-content: center;
  }

  .company-name {
    position: absolute;
    left: 34px; top: 34px;
    font-weight: 600;
    font-size: 30px;
    line-height: 1;
    color: var(--brand-purple);
  }

  .address {
    position: absolute;
    left: 34px; top: 112px;
    font-size: 12px;
    line-height: 1.35;
    color: var(--text-muted);
  }

  .contact-list {
    position: absolute;
    left: 34px; bottom: 28px;
    list-style: none;
    font-size: 12px;
    line-height: 1;
    color: var(--text-light);
  }
  .contact-list li { display: flex; align-items: center; gap: 8px; margin-top: 7px; }
  .contact-list svg { width: 11px; height: 11px; flex: none; }

  .person {
    position: absolute;
    right: 40px; bottom: 38px;
    text-align: right;
  }
  .person__name {
    font-family: "Montserrat", Arial, sans-serif;
    font-weight: 700;
    font-size: 22px;
    color: var(--brand-pink);
  }
  .person__role {
    margin-top: 2px;
    font-size: 14px;
    color: var(--text-light);
  }
  .edge-bar {
    position: absolute;
    right: 0; bottom: 30px;
    width: 22px; height: 52px;
    background: var(--brand-pink);
  }

  .back-name {
    font-weight: 600;
    font-size: 56px;
    line-height: 1;
    color: var(--emboss);
  }
</style>
</head>
<body>

  <section class="card card--front" aria-label="Business card front">
    <div class="company-name">Velmora</div>

    <p class="address">Sample City, 1234 NSW<br>Australia</p>

    <ul class="contact-list">
      <li>
        <svg viewBox="0 0 12 12" aria-hidden="true"><rect x="3" y="0.8" width="6" height="10.4" rx="1" fill="none" stroke="var(--brand-pink)" stroke-width="1.2"/></svg>
        0412558903
      </li>
      <li>
        <svg viewBox="0 0 12 12" aria-hidden="true"><path d="M2.5 1.5l2 2-1 1.2c.7 1.5 1.8 2.6 3.3 3.3l1.2-1 2 2-1.3 1.5C5 10.2 1.8 7 1 3z" fill="var(--brand-pink)"/></svg>
        1300 727 415
      </li>
      <li>
        <svg viewBox="0 0 12 12" aria-hidden="true"><g fill="none" stroke="var(--brand-pink)" stroke-width="1.1"><circle cx="6" cy="6" r="5"/><ellipse cx="6" cy="6" rx="2.2" ry="5"/><path d="M1 6h10"/></g></svg>
        www.velmoracare.com.au
      </li>
      <li>
        <svg viewBox="0 0 12 12" aria-hidden="true"><g fill="none" stroke="var(--brand-pink)" stroke-width="1.1"><rect x="1" y="2.5" width="10" height="7" rx="1"/><path d="M1.3 3l4.7 3.6L10.7 3"/></g></svg>
        daniel.hartwell@velmoracare.com.au
      </li>
    </ul>

    <div class="person">
      <div class="person__name">Daniel Hartwell</div>
      <div class="person__role">CEO</div>
    </div>
    <div class="edge-bar"></div>
  </section>

  <section class="card card--back" aria-label="Business card back">
    <div class="back-name">Velmora</div>
  </section>

</body>
</html>
```